Marlow Guard Shop Signage with provided LOGO

Need 2 designs (1) indicating the store is around the corner horizontal format and (1) in a vertical format without the around the corner indication. HD image for a 24" by 60" sign. Use attached image for inspiration. Our business of on the south side of a large building and we need to have 2 signs on the front of the build indicating LEFT and the last sign will be a sidewalk sign next to our business.

Industry/Entity Type

Security

Font styles to use
Serif

Colors
33a6d7

Requirements
Must have
• WEBSITE URL: www.dwellsafedepot.com and www.marlowguardshop.com they can be in small font.
Nice to have
• Phone Number (833) 562-9184

```html
<!DOCTYPE html>
<html lang="en">
<head>
<meta charset="UTF-8">
<title>Marlow Guard Shop – Vertical Sign</title>
<link rel="stylesheet" href="https://fonts.googleapis.com/css2?family=Marcellus&display=swap">
<style>
  :root {
    --sign-blue: #33a6d7;
    --deep-blue: #0057a8;
    --text-white: #ffffff;
    --page-bg: #ffffff;
  }
  * { margin: 0; padding: 0; box-sizing: border-box; }
  html, body {
    width: 1200px;
    height: 1200px;
    overflow: hidden;
    background: var(--page-bg);
  }
  .canvas {
    position: relative;
    width: 1200px;
    height: 1200px;
  }
  .sign {
    position: absolute;
    left: 387px;
    top: 67px;
    width: 427px;
    height: 1066px;
    background: var(--sign-blue);
    font-family: "Marcellus", serif;
    color: var(--text-white);
    overflow: hidden;
  }
  .edge-bar {
    position: absolute;
    right: 0;
    width: 29px;
    background: var(--deep-blue);
  }
  .edge-bar--top { top: 0; height: 253px; }
  .edge-bar--middle { top: 279px; height: 508px; }
  .edge-bar--bottom { top: 813px; bottom: 0; }
  .edge-tab {
    position: absolute;
    left: 0;
    width: 12px;
    height: 25px;
    background: var(--deep-blue);
  }
  .edge-tab--upper { top: 254px; }
  .edge-tab--lower { top: 787px; }
  .content {
    position: absolute;
    left: 0;
    width: 398px;
    text-align: center;
  }
  .brand-mark {
    position: absolute;
    left: 99px;
    top: 41px;
    width: 200px;
    height: 200px;
  }
  .brand-name {
    top: 270px;
    color: var(--deep-blue);
    line-height: 1;
  }
  .brand-name__main {
    display: block;
    font-size: 76px;
    letter-spacing: 1px;
  }
  .brand-name__sub {
    display: block;
    margin-top: 14px;
    font-size: 42px;
    letter-spacing: 1px;
  }
  .tagline {
    top: 609px;
    font-size: 52px;
    line-height: 62px;
    letter-spacing: 1px;
  }
  .web-links {
    top: 990px;
    font-size: 17px;
    line-height: 24px;
    letter-spacing: 0.3px;
  }
  .phone {
    top: 1066px;
    font-size: 38px;
    line-height: 1;
    letter-spacing: 1px;
  }
</style>
</head>
<body>
<main class="canvas">
  <section class="sign" aria-label="Marlow Guard Shop vertical sign">
    <div class="edge-bar edge-bar--top"></div>
    <div class="edge-bar edge-bar--middle"></div>
    <div class="edge-bar edge-bar--bottom"></div>
    <div class="edge-tab edge-tab--upper"></div>
    <div class="edge-tab edge-tab--lower"></div>

    <svg class="brand-mark" viewBox="0 0 200 200" aria-hidden="true">
      <circle cx="100" cy="100" r="100" fill="#0057a8"/>
    </svg>

    <h1 class="content brand-name">
      <span class="brand-name__main">MARLOW</span>
      <span class="brand-name__sub">GUARD SHOP</span>
    </h1>

    <p class="content tagline">SECURITY<br>&amp;<br>SURVEILLANCE<br>PRODUCTS</p>

    <p class="content web-links">www.dwellsafedepot.com<br>www.marlowguardshop.com</p>

    <p class="content phone">(833) 562-9184</p>
  </section>
</main>
</body>
</html>
```